Modern Label for Loose Tea pouches on 4.5x6 Label

We need a new label for our teas that is very simple in design, but stylish and modern. This will be used to print labels for our loose tea pouches. The label will be at max 4.5x6 inches in size. There should be a place for the tea name, description, ingredients, and size that is changeable.
Preferably an AI file that allows me to setup variables to change the above items. There will also need to be our logo which is supplied, and our address on the label.
Address:
Orvessa Leaf
846 Lower Maple Lane
Larkhaven, ME 04917
Target Market(s)
Tea Lovers
Requirements
Must have
- Adobe Illustrator file with variables setup for replacement of tea name, description, ingredients, and size (weights 2oz, 4oz, 8oz, 1lb)

```html
<!DOCTYPE html>
<html lang="en">
<head>
<meta charset="utf-8">
<title>Orvessa Leaf – Chamomile Loose Tea Label</title>
<link rel="stylesheet" href="https://fonts.googleapis.com/css2?family=Federant&family=Federo&family=Kreon:wght@400;700&family=Pathway+Gothic+One&family=Roboto+Condensed:wght@400;700&family=Andada+Pro&display=swap">
<style>
  :root {
    --cream: #f6f3d6;
    --pink: #df5aa6;
    --green: #b5d335;
    --green-shade: #8ea428;
    --page: #ffffff;
  }
  * { box-sizing: border-box; margin: 0; padding: 0; }
  html, body { width: 1200px; height: 778px; overflow: hidden; background: var(--page); }
  .canvas { position: relative; width: 1200px; height: 778px; }

  .label {
    position: absolute; left: 305px; top: 164px;
    width: 590px; height: 450px;
    background: var(--cream);
  }
  .label__frame {
    position: absolute; inset: 8px;
    border: 2px solid var(--pink);
  }
  .rule { position: absolute; }
  .rule--top-pink { left: 33px; width: 528px; top: 34px; height: 5px; background: var(--pink); }
  .rule--top-green { left: 45px; width: 504px; top: 41px; height: 3px; background: var(--green); }
  .rule--bottom-green { left: 45px; width: 504px; top: 364px; height: 3px; background: var(--green); }
  .rule--bottom-pink { left: 33px; width: 528px; top: 370px; height: 5px; background: var(--pink); }

  .brand {
    position: absolute; left: 0; right: 0; top: 100px;
    display: flex; justify-content: center; align-items: center; gap: 10px;
  }
  .brand__dot { width: 14px; height: 14px; border-radius: 50%; background: var(--green); }
  .brand__name {
    font-family: "Kreon", serif; font-weight: 700;
    font-size: 30px; letter-spacing: 0.5px; color: var(--pink);
  }
  .brand-underline { left: 195px; width: 200px; top: 140px; height: 2px; background: var(--green); }

  .product-type {
    position: absolute; left: 0; right: 0; top: 150px; text-align: center;
    font-family: "Federo", sans-serif; font-size: 30px; color: var(--pink);
    letter-spacing: 1px;
  }
  .tea-name {
    position: absolute; left: 0; right: 0; top: 190px; text-align: center;
    font-family: "Federant", serif; font-size: 66px; font-weight: 400; letter-spacing: 3px;
    color: var(--pink);
    -webkit-text-stroke: 2px var(--green);
    paint-order: stroke fill;
  }
  .ribbon { position: absolute; left: 122px; top: 276px; width: 366px; height: 90px; }
  .description {
    position: absolute; left: 162px; top: 282px; width: 286px; height: 62px;
    display: flex; align-items: center; justify-content: center; text-align: center;
    font-family: "Andada Pro", serif; font-size: 16.5px; line-height: 1.08;
    color: var(--cream);
  }
  .address {
    position: absolute; left: 33px; top: 382px;
    font-family: "Roboto Condensed", sans-serif; font-size: 11.5px; line-height: 1.15;
    color: var(--pink); font-style: normal;
  }
  .address__name { font-weight: 700; font-size: 13px; }
  .servings, .net-weight {
    position: absolute; top: 386px;
    font-family: "Pathway Gothic One", sans-serif; font-size: 32px; color: var(--pink);
  }
  .servings { left: 195px; }
  .net-weight { left: 440px; }
</style>
</head>
<body>
<main class="canvas">
  <section class="label">
    <div class="label__frame"></div>
    <div class="rule rule--top-pink"></div>
    <div class="rule rule--top-green"></div>

    <div class="brand">
      <span class="brand__dot"></span>
      <span class="brand__name">ORVESSA LEAF</span>
    </div>
    <div class="rule brand-underline"></div>

    <p class="product-type">LOOSE TEA</p>
    <h1 class="tea-name">CHAMOMILE</h1>

    <svg class="ribbon" viewBox="0 0 366 90" aria-hidden="true">
      <polygon points="0,28 40,28 40,82 0,82 14,55" fill="var(--green)"/>
      <polygon points="366,28 326,28 326,82 366,82 352,55" fill="var(--green)"/>
      <polygon points="30,68 30,82 40,82" fill="var(--green-shade)"/>
      <polygon points="336,68 336,82 326,82" fill="var(--green-shade)"/>
      <rect x="30" y="6" width="306" height="62" fill="var(--pink)"/>
    </svg>
    <p class="description">Hand picked from the optimum part of the plant for flavor and health benefits</p>

    <div class="rule rule--bottom-green"></div>
    <div class="rule rule--bottom-pink"></div>

    <address class="address">
      <span class="address__name">Orvessa Leaf</span><br>
      846 Lower Maple Lane<br>
      Larkhaven, ME 04917
    </address>
    <p class="servings">MAKES 50 SERVINGS</p>
    <p class="net-weight">NET WT 4 Oz.</p>
  </section>
</main>
</body>
</html>
```